Food Safety Consultancy Flyer Design

We need a flyer design for a new company called Tundo Training. New food safety regulations are coming into effect for all food operators in March 2016. My company provides training and resources to support food operators during the transition onto the new Food Control Plan. For the designs we would like to see any of the colours used from the logo which is attached. The flyer will be letting operators know that there are new regulations and we are here to help. Our company offers three packages: 1. Videos (training videos) 2. Webinars and Workshop 3. One-on-one mentoring. Our websites main colour used is the green colour from the logo.
Food service operators: cafes, restaurants etc.
Hospitality

```html
<!DOCTYPE html>
<html lang="en">
<head>
<meta charset="utf-8">
<title>Tundo Training – Food Act 2014 Flyer</title>
<link href="https://fonts.googleapis.com/css2?family=Montserrat:wght@400;500;600;700&family=Roboto+Condensed:ital,wght@1,700&family=Nunito:wght@800&family=Didact+Gothic&display=swap" rel="stylesheet">
<style>
  :root {
    --green: #3cb54a;
    --green-light: #5cc766;
    --blue: #1f6fb8;
    --blue-bright: #2a7fd0;
    --ink: #1c1c1c;
    --grey-bg: #f2f2f2;
    --grey-line: #d9d9d9;
    --white: #ffffff;
  }
  html, body { margin: 0; padding: 0; overflow: hidden; background: var(--white); }
  .flyer {
    position: relative; width: 990px; height: 1200px; overflow: hidden;
    background: var(--white); font-family: "Montserrat", sans-serif; color: var(--ink);
  }
  .hero-band { position: absolute; left: 0; top: 0; width: 990px; height: 420px; }
  .tagline-top {
    position: absolute; top: 26px; left: 0; width: 100%; margin: 0;
    text-align: center; color: var(--white);
    font-family: "Roboto Condensed", sans-serif; font-style: italic; font-weight: 700; font-size: 30px;
  }
  .chef {
    position: absolute; border-radius: 80px 80px 16px 16px;
    background: linear-gradient(180deg, #f4f4f4 0%, #e3e3e3 60%, #bdbdbd 100%);
  }
  .chef--left { left: 55px; top: 70px; width: 185px; height: 410px; }
  .chef--right { left: 760px; top: 70px; width: 170px; height: 410px; }
  .act-badge {
    position: absolute; left: 360px; top: 96px; width: 250px; height: 250px;
    border-radius: 50%; background: var(--white);
    box-shadow: 0 0 0 12px var(--green-light);
    text-align: center; font-family: "Didact Gothic", sans-serif;
  }
  .act-badge__title { margin: 40px 0 0; color: var(--blue); font-size: 38px; line-height: 1; }
  .act-badge__year { margin: 0; color: var(--blue); font-size: 64px; line-height: 1; letter-spacing: 2px; }
  .act-badge__rule { width: 170px; margin: 6px auto 4px; border-top: 2px dashed #333; }
  .act-badge__note { margin: 0; color: var(--green); font-size: 21px; line-height: 1.2; }
  .act-badge__date { margin: 2px 0 0; color: var(--ink); font-size: 28px; line-height: 1.1; }
  .brand {
    position: absolute; top: 410px; left: 0; width: 100%;
    display: flex; justify-content: center; align-items: center; gap: 14px;
  }
  .brand__dot { width: 30px; height: 30px; border-radius: 50%; background: var(--green); }
  .brand__name {
    font-weight: 600; font-size: 44px; line-height: 1; letter-spacing: 4px;
    color: var(--ink); text-transform: uppercase;
  }
  .intro {
    position: absolute; top: 545px; left: 120px; width: 750px; margin: 0;
    text-align: center; font-size: 17px; line-height: 1.4;
  }
  .knowledge-lead {
    position: absolute; top: 618px; left: 0; width: 100%; margin: 0;
    text-align: center; font-size: 23px;
  }
  .topics {
    position: absolute; top: 650px; left: 60px; width: 870px; margin: 0;
    text-align: center; color: var(--blue-bright); font-weight: 600; font-size: 21px; line-height: 31px;
  }
  .lower-field { position: absolute; left: 0; top: 725px; width: 990px; height: 420px; }
  .service { position: absolute; top: 745px; width: 320px; text-align: center; }
  .service--videos { left: 35px; }
  .service--webinars { left: 350px; }
  .service--mentoring { left: 641px; }
  .service__icon {
    width: 92px; height: 92px; margin: 0 auto; border-radius: 50%;
    background: var(--green); display: flex; align-items: center; justify-content: center;
  }
  .service__title {
    margin: 14px 0 6px; color: var(--green); font-family: "Nunito", sans-serif;
    font-weight: 800; font-size: 23px; line-height: 1.1;
  }
  .service__text { margin: 0; font-size: 15px; font-weight: 600; line-height: 21px; }
  .service__rule { width: 120px; margin: 5px auto; border-top: 1px dashed #888; }
  .corner-block { position: absolute; top: 1092px; width: 60px; height: 50px; background: var(--green); }
  .corner-block--left { left: 0; }
  .corner-block--right { right: 0; }
  .closing {
    position: absolute; top: 1098px; left: 0; width: 100%; margin: 0;
    text-align: center; font-family: "Roboto Condensed", sans-serif;
    font-style: italic; font-weight: 700; font-size: 30px; line-height: 36px; color: var(--ink);
  }
  .closing em { color: var(--green); }
  .footer {
    position: absolute; left: 0; bottom: 0; width: 100%; height: 58px;
    background: var(--blue); color: var(--white);
    display: flex; align-items: center; justify-content: center;
    font-family: "Roboto Condensed", sans-serif; font-style: italic; font-weight: 700; font-size: 26px;
  }
  .footer__sep { margin: 0 12px; }
</style>
</head>
<body>
<div class="flyer">

  <svg class="hero-band" viewBox="0 0 990 420" aria-hidden="true">
    <defs>
      <radialGradient id="rays" cx="50%" cy="45%" r="70%">
        <stop offset="0" stop-color="#5dc868"/>
        <stop offset="1" stop-color="#35ad45"/>
      </radialGradient>
    </defs>
    <path d="M0 0 H990 V150 C820 250 650 340 495 350 C330 360 150 320 0 260 Z" fill="url(#rays)"/>
    <g fill="#ffffff" opacity="0.07">
      <path d="M495 230 L0 0 H120 Z"/><path d="M495 230 L260 0 H380 Z"/>
      <path d="M495 230 L560 0 H680 Z"/><path d="M495 230 L820 0 H940 Z"/>
      <path d="M495 230 L990 110 V200 Z"/><path d="M495 230 L0 140 V220 Z"/>
    </g>
    <path d="M990 150 C820 250 650 340 495 350 C650 352 820 290 990 200 Z" fill="var(--blue-bright)"/>
  </svg>

  <p class="tagline-top">Your reputation is our business</p>

  <div class="chef chef--left" role="img" aria-label="Illustrated chef holding a ladle and a cooking pot"></div>
  <div class="chef chef--right" role="img" aria-label="Illustrated chef carrying a covered serving dish"></div>

  <div class="act-badge">
    <p class="act-badge__title">Food Act</p>
    <p class="act-badge__year">2014</p>
    <div class="act-badge__rule"></div>
    <p class="act-badge__note">comes into force on</p>
    <p class="act-badge__date">1 March 2016</p>
  </div>

  <div class="brand">
    <span class="brand__dot"></span>
    <span class="brand__name">Tundo Training</span>
  </div>

  <p class="intro">Food service and food retailers will be on Food Control Plans – documentation<br>of processes and risk management to produce safe and suitable food.</p>

  <p class="knowledge-lead">With up-to-date knowledge on:</p>
  <p class="topics">The Food Act 2014 | Food Control Plan requirements |<br>Verification expectations | New Food Grading System | New Fees</p>

  <svg class="lower-field" viewBox="0 0 990 420" aria-hidden="true">
    <path d="M0 40 C250 -5 740 -5 990 40 V420 H0 Z" fill="var(--grey-bg)"/>
    <path d="M0 40 C250 -5 740 -5 990 40" fill="none" stroke="var(--grey-line)" stroke-width="4"/>
  </svg>

  <article class="service service--videos">
    <div class="service__icon">
      <svg width="56" height="38" viewBox="0 0 60 40" aria-hidden="true">
        <rect x="4" y="8" width="36" height="26" rx="4" fill="#fff"/>
        <path d="M40 16 L56 8 V34 L40 26 Z" fill="#fff"/>
        <circle cx="14" cy="5" r="5" fill="#fff"/><circle cx="28" cy="5" r="5" fill="#fff"/>
      </svg>
    </div>
    <h2 class="service__title">Videos</h2>
    <p class="service__text">Animated training<br>videos of the FCP</p>
    <div class="service__rule"></div>
    <p class="service__text">6 month subscription</p>
    <div class="service__rule"></div>
    <p class="service__text">Translated into Mandarin,<br>Japanese, Korean and<br>Hindi</p>
  </article>

  <article class="service service--webinars">
    <div class="service__icon">
      <svg width="56" height="48" viewBox="0 0 60 50" aria-hidden="true">
        <rect x="10" y="14" width="40" height="26" rx="2" fill="none" stroke="#fff" stroke-width="4"/>
        <path d="M4 42 H56 L52 47 H8 Z" fill="#fff"/>
        <rect x="30" y="2" width="22" height="13" rx="3" fill="#fff"/>
        <circle cx="36" cy="8.5" r="1.5" fill="var(--green)"/><circle cx="41" cy="8.5" r="1.5" fill="var(--green)"/><circle cx="46" cy="8.5" r="1.5" fill="var(--green)"/>
      </svg>
    </div>
    <h2 class="service__title">Webinars/Workshops</h2>
    <p class="service__text">A range of webinars<br>at times to suit the<br>hospitality industry AND<br>half day training workshops.</p>
    <div class="service__rule"></div>
    <p class="service__text">6 month subscription<br>to the video library<br>is included</p>
  </article>

  <article class="service service--mentoring">
    <div class="service__icon" role="img" aria-label="Mentoring illustration of one person helping another up a step"></div>
    <h2 class="service__title">Mentoring</h2>
    <p class="service__text">We come to you<br>and go through the<br>FCP page-by-page</p>
  </article>

  <div class="corner-block corner-block--left"></div>
  <div class="corner-block corner-block--right"></div>

  <p class="closing"><em>Let us help you</em> transition and understand <em>all there is to know.</em></p>

  <footer class="footer">
    <span>www.tundotraining.co.nz</span><span class="footer__sep">|</span><span>info@tundotraining.co.nz</span>
  </footer>
</div>
</body>
</html>
```